Fiber Optic Internet flyer promotion Winter 2016-2017

I am looking for a marketing flyer that will not be folded, single sided that will advertise a Fiber Optic internet promotion that we are currently running.

The design should be clean, flow well, quickly grab attention, and if a very few short seconds list what the promotion is, and direct them to contact us.

It needs to list a few features of the promotion, but does not need to be in this order and should flow well with the flyer
1.) Fiber Optic Internet
2.) 100 Mbits for $140 /month or 150 Mbits for $190 /month
3.) Free construction cost up to $10,000, limited funds available.
4.) Limited time offer. Must commit before funds run out.

(555) 274-3619, www.kelvaroute.net

Target Market(s)

Small to large business

Industry/Entity Type

Internet Service Provider

Requirements
Must have
• Eye catching appeal. Quickly convey the message of the promotion and our company name and phone number.
Should not have
• Our company is primarily a wireless ISP. This promotion is all about Fiber Optic. I do not want to draw attention to the "wireless" portion of our business with this flyer.

```html
<!DOCTYPE html>
<html lang="en">
<head>
<meta charset="utf-8">
<title>Kelvaroute Networks – Fiber Optic Internet Flyer</title>
<link href="https://fonts.googleapis.com/css2?family=Roboto+Slab:wght@700;800&family=Open+Sans:wght@400;700;800&display=swap" rel="stylesheet">
<style>
  :root {
    --backdrop: #e9e8e8;
    --paper: #ffffff;
    --navy: #1c3461;
    --red: #d42233;
    --sky: #0fa7e6;
    --lime: #7cc242;
    --orange: #f15a29;
    --teal: #1aaa9c;
    --ink-light: #ffffff;
  }
  * { box-sizing: border-box; margin: 0; padding: 0; }
  html, body { width: 1200px; height: 800px; overflow: hidden; }
  body {
    background: var(--backdrop);
    font-family: "Open Sans", Arial, sans-serif;
    position: relative;
  }
  .flyer {
    position: absolute;
    left: 340px; top: 30px;
    width: 520px; height: 740px;
    background: var(--paper);
    overflow: hidden;
    box-shadow: 0 6px 18px rgba(0,0,0,.18);
  }
  .header { position: absolute; left: 0; top: 0; width: 100%; height: 86px; }
  .brand {
    position: absolute; left: 30px; top: 30px;
    display: flex; align-items: center; gap: 8px;
  }
  .brand-dot { width: 20px; height: 20px; border-radius: 50%; background: var(--red); }
  .brand-name {
    font-weight: 800; font-size: 19px; color: var(--navy);
    letter-spacing: .5px; text-transform: uppercase;
  }
  .corner { position: absolute; right: 0; top: 0; }
  .hero-photo {
    position: absolute; left: 0; top: 86px; width: 100%; height: 290px;
    background: linear-gradient(135deg, #0d1e3a 0%, #2c4f7a 45%, #6b7f95 70%, #1e3555 100%);
  }
  .title-rule { position: absolute; left: 0; top: 376px; width: 100%; height: 5px; background: var(--red); }
  .title-band {
    position: absolute; left: 0; top: 381px; width: 318px; height: 74px;
    background: var(--navy);
    display: flex; align-items: center; justify-content: center;
  }
  .title {
    font-family: "Roboto Slab", Georgia, serif; font-weight: 800;
    color: var(--ink-light); font-size: 27px; letter-spacing: 1px; white-space: nowrap;
  }
  .fiber-photo {
    position: absolute; left: 200px; top: 455px; width: 120px; height: 155px;
    background: radial-gradient(circle at 50% 40%, #e0313a 0%, #8e0f18 55%, #3a0508 100%);
  }
  .tile { position: absolute; color: var(--ink-light); display: flex; align-items: center; justify-content: center; text-align: center; }
  .tile-price { left: 318px; top: 381px; width: 202px; height: 110px; background: var(--sky); font-size: 14px; line-height: 1.3; }
  .tile-offer { left: 318px; top: 491px; width: 202px; height: 119px; background: var(--lime); font-size: 14px; line-height: 1.3; }
  .tile-fiber { left: 0; top: 455px; width: 200px; height: 120px; background: var(--orange); font-size: 16px; font-weight: 700; line-height: 1.2; }
  .tile-build { left: 0; top: 575px; width: 200px; height: 105px; background: var(--teal); font-size: 15px; line-height: 1.3; }
  .tile b { font-weight: 800; }
  .laptop-photo {
    position: absolute; left: 200px; top: 610px; width: 320px; height: 70px;
    background: linear-gradient(90deg, #d9d4cc 0%, #f3f0ea 50%, #c93a3a 80%, #e8e2da 100%);
  }
  .contact-band {
    position: absolute; left: 0; top: 680px; width: 100%; height: 60px;
    background: var(--navy); color: var(--ink-light);
    display: flex; align-items: center; justify-content: center; gap: 14px;
    font-family: "Roboto Slab", Georgia, serif; font-weight: 700;
  }
  .phone { font-size: 25px; }
  .divider { font-size: 22px; }
  .web { font-size: 19px; }
</style>
</head>
<body>
  <article class="flyer">
    <header class="header">
      <div class="brand">
        <span class="brand-dot"></span>
        <span class="brand-name">Kelvaroute Networks</span>
      </div>
      <svg class="corner" width="200" height="86" viewBox="0 0 200 86" aria-hidden="true">
        <polygon points="40,86 120,0 200,0 200,86" fill="#1c3461"/>
        <polygon points="70,86 150,0 200,0 200,86" fill="#d42233"/>
      </svg>
    </header>

    <div class="hero-photo" role="img" aria-label="Technician with a tablet working at a server rack in a data center"></div>

    <div class="title-rule"></div>
    <div class="title-band"><h1 class="title">INTERNET SOLUTION</h1></div>

    <div class="tile tile-price"><p><b>100 Mbits</b> for<br><b>$140</b> per month<br>or <b>150 Mbits</b> for<br><b>$190</b> per month</p></div>
    <div class="fiber-photo" role="img" aria-label="Glowing red fiber optic strands"></div>
    <div class="tile tile-offer"><p>Limited time<br>offer. Must<br>commit before<br>funds <b>run out</b></p></div>

    <div class="tile tile-fiber"><p>Fiber Optic<br>Internet</p></div>
    <div class="tile tile-build"><p>Free construction<br>cost up to<br><b>$10,000</b>, limited<br>funds available.</p></div>
    <div class="laptop-photo" role="img" aria-label="Woman lying on a sofa using a laptop"></div>

    <footer class="contact-band">
      <span class="phone">(555) 274-3619</span>
      <span class="divider">|</span>
      <span class="web">www.kelvaroute.net</span>
    </footer>
  </article>
</body>
</html>
```